New Meal Prep Flyer for New Package Deals

We are looking for a design that displays our new packages that we offer. If you take a look at our website www.brambleforkmeals.com, and click on packages , you'll see the way we display them currently . We would like something similar to that in style . The first package is called "Horizon" and this package will be a 1 week package (7 days ), 2 meals a day, for a price of $195.00. The second package is called "Amber" and this package will be a 3 week package (21 days) 2 meals per day, for a price of $546.00 , the third package is a 6 week+ package (45 days), and it is called "Evergreen" , 2 meals per day , and the price is $1080.00 .
For the Amber Package , can you put next to it "Save $42.00!"
For the Evergreen Package, can you put next to it "Save $180!"
We also want our logo on the flyer (see attached), and we are just looking for a 1 page flyer , 8 1/2 x 11.

```html
<!DOCTYPE html>
<html lang="en">
<head>
<meta charset="utf-8">
<title>Bramblefork – New Packages</title>
<link rel="stylesheet" href="https://fonts.googleapis.com/css2?family=Montserrat:wght@500;600;700&family=Oswald:wght@500;600&display=swap">
<style>
:root{
  --page:#000000;
  --paper:#f4f4f4;
  --white:#ffffff;
  --green:#8cc21f;
  --green-deep:#5f9618;
  --green-text:#5c8f17;
  --grey:#7a7a7a;
  --grey-deep:#565656;
  --grey-text:#5a5a5a;
  --orange:#f2a01c;
  --orange-deep:#d9690b;
  --orange-text:#d8680c;
  --ink-soft:#8a8a8a;
  --badge:#3a3a3a;
}
*{margin:0;padding:0;box-sizing:border-box}
html,body{width:1200px;height:1200px;overflow:hidden;background:var(--page)}
.flyer{position:absolute;left:204px;top:74px;width:810px;height:1052px;overflow:hidden;
  background:linear-gradient(160deg,#f7f7f7 0%,#e2e2e2 50%,#f3f3f3 100%);font-family:"Montserrat",sans-serif}
.backdrop{position:absolute;inset:0}
.brand{position:absolute;left:22px;top:30px;display:flex;align-items:center;gap:12px}
.brand-dot{width:26px;height:26px;border-radius:50%;background:var(--green)}
.brand-name{font-weight:600;font-size:44px;color:var(--grey-text);letter-spacing:1px}
.headline{position:absolute;left:450px;width:340px;top:26px;text-align:center;color:var(--white);font-weight:600;line-height:1.05}
.headline .new{display:block;font-size:66px;letter-spacing:1px}
.headline .packages{display:block;font-size:60px}

.package{position:absolute;top:406px;width:250px;height:420px}
.package.horizon{left:24px;--main:var(--green);--main-deep:var(--green-deep);--accent:var(--green-text)}
.package.amber{left:282px;--main:var(--grey);--main-deep:var(--grey-deep);--accent:var(--grey-text)}
.package.evergreen{left:542px;--main:var(--orange);--main-deep:var(--orange-deep);--accent:var(--orange-text)}
.save{position:absolute;right:0;top:-64px;width:140px;height:58px;border-radius:36px 0 0 0;
  background:var(--main-deep);color:var(--white);font-size:17px;font-weight:600;text-align:center;line-height:1.15;padding-top:7px}
.amber .save{background:#6b6b6b}
.evergreen .save{background:linear-gradient(90deg,var(--orange-deep),var(--orange))}
.strip{position:absolute;left:0;top:86px;width:44px;height:334px;border-radius:40px 0 0 0;background:var(--main-deep)}
.strip-label{position:absolute;left:22px;bottom:22px;transform:rotate(-90deg);transform-origin:0 0;
  white-space:nowrap;color:var(--white);font-size:22px;font-weight:600;letter-spacing:1px;text-transform:uppercase;
  translate:-13px 0}
.price-tab{position:absolute;left:48px;top:0;width:202px;height:110px;background:var(--white);border-radius:62px 0 0 0;
  text-align:right;padding:8px 14px 0 0;font-family:"Oswald",sans-serif;font-weight:600;color:var(--accent)}
.price-tab .amount{font-size:48px;letter-spacing:-1px}
.price-tab .cents{font-size:26px}
.main{position:absolute;left:52px;top:78px;width:198px;height:342px;border-radius:70px 0 48px 0;
  background:linear-gradient(135deg,var(--main) 0%,var(--main-deep) 100%);color:var(--white);text-align:center}
.evergreen .main{background:linear-gradient(200deg,var(--orange-deep) 0%,var(--orange) 100%)}
.amber .main{background:linear-gradient(200deg,#5e5e5e 0%,#9a9a9a 100%)}
.term{display:inline-block;margin-top:74px;background:var(--white);color:var(--accent);font-weight:700;font-size:27px;padding:4px 14px}
.detail{font-size:21px;font-weight:600;line-height:1.4}
.detail.days{margin-top:14px}
.detail.meals{margin-top:28px}

.store-badge{position:absolute;left:114px;width:154px;height:44px;border-radius:8px;background:var(--badge);border:2px solid #bdbdbd}
.store-badge.first{top:900px}
.store-badge.second{top:952px;background:var(--white);border-color:#cfcfcf}
.call-icon{position:absolute;left:578px;top:936px;width:48px;height:48px}
.site{position:absolute;left:380px;width:440px;top:990px;text-align:center;color:var(--white);font-weight:600;font-size:33px}
</style>
</head>
<body>
<main class="flyer">
  <svg class="backdrop" viewBox="0 0 810 1052" width="810" height="1052" aria-hidden="true">
    <defs>
      <linearGradient id="greenFill" x1="0" y1="0" x2="1" y2="1">
        <stop offset="0" stop-color="#a6d22c"/><stop offset="1" stop-color="#6ea71a"/>
      </linearGradient>
    </defs>
    <path d="M0,0 H810 V258 C640,300 420,190 0,176 Z" fill="url(#greenFill)"/>
    <path d="M0,0 H420 C500,30 470,140 300,165 C180,180 80,160 0,170 Z" fill="#ffffff"/>
    <path d="M0,200 C240,170 460,260 810,262 V300 C500,300 260,220 0,232 Z" fill="#ffffff"/>
    <path d="M0,1052 V900 C200,860 520,820 810,850 V870 C560,850 260,900 0,960 Z" fill="#ffffff"/>
    <path d="M0,1052 V960 C260,900 560,850 810,870 V1052 Z" fill="url(#greenFill)"/>
  </svg>

  <div class="brand"><span class="brand-dot"></span><span class="brand-name">Bramblefork</span></div>
  <h1 class="headline"><span class="new">NEW</span><span class="packages">Packages</span></h1>

  <section class="package horizon">
    <div class="strip"><span class="strip-label">★ Horizon ★</span></div>
    <div class="main">
      <div class="term">1 WEEK</div>
      <p class="detail days">package<br>(7 days )</p>
      <p class="detail meals">2 meals<br>a day</p>
    </div>
    <div class="price-tab"><span class="amount">$195</span><span class="cents">.00</span></div>
  </section>

  <section class="package amber">
    <div class="save">Save<br>$42.00!</div>
    <div class="strip"><span class="strip-label">★ Amber ★</span></div>
    <div class="main">
      <div class="term">3 WEEK</div>
      <p class="detail days">package<br>(21 days )</p>
      <p class="detail meals">2 meals<br>a day</p>
    </div>
    <div class="price-tab"><span class="amount">$546</span><span class="cents">.00</span></div>
  </section>

  <section class="package evergreen">
    <div class="save">Save<br>$180.00!</div>
    <div class="strip"><span class="strip-label">★ Evergreen ★</span></div>
    <div class="main">
      <div class="term">6+ WEEK</div>
      <p class="detail days">package<br>(45 days )</p>
      <p class="detail meals">2 meals<br>a day</p>
    </div>
    <div class="price-tab"><span class="amount">$1080</span><span class="cents">.00</span></div>
  </section>

  <div class="store-badge first" role="img" aria-label="App store download badge"></div>
  <div class="store-badge second" role="img" aria-label="App store download badge"></div>

  <svg class="call-icon" viewBox="0 0 48 48" aria-hidden="true">
    <circle cx="24" cy="24" r="24" fill="#ffffff"/>
    <path d="M17 13 l5 0 2 7 -3 2 c1.5 3.5 3.5 5.5 7 7 l2 -3 7 2 0 5 c-12 1 -20 -8 -20 -20 z" fill="#6ea71a"/>
    <path d="M27 14 a8 8 0 0 1 7 7 M27 18 a4 4 0 0 1 3 3" stroke="#6ea71a" stroke-width="2" fill="none" stroke-linecap="round"/>
  </svg>
  <p class="site">brambleforkmeals.com</p>
</main>
</body>
</html>
```